Online Marketing Agency Website

We are an online marketing agency that specializes in search marketing (SEM) for businesses of all sizes. Our core services include local search marketing, seo, paid search, paid social, graphic design, video production/editing and website design. We have an existing website that we launched a number of years ago but it's very outdated and we're currently too busy to design a new version.

Target Market(s)

Any business that needs online marketing services with an emphasis on search marketing.

Industry/Entity Type

Ad Agency

Number of Pages Required

4 page

Font styles to use
Sans Serif

Requirements
Must have
• Home page, interior page, blog page, contact us page.
Look and feel should be modern and clean and easy to navigate.
Sections for call outs for specific services: Business Marketing Strategy, Content Creation and Marketing, Graphic & Publication Design, Pay Per Click (PPC) Management, Search Engine Optimization, Social Media Management, Video Production & Editing, Website Hosting & Management, Website Design & Development
Use color from logo that was uploaded.

```html
<!DOCTYPE html>
<html lang="en">
<head>
<meta charset="utf-8">
<title>Contact Us – Liftwave Media</title>
<link href="https://fonts.googleapis.com/css2?family=Poppins:wght@300;400;500;600;700&display=swap" rel="stylesheet">
<style>
:root{
  --orange:#ff4707;
  --ink:#2f2f2f;
  --muted:#555;
  --field:#f4f4f4;
  --dark:#333333;
  --rule:#e6e6e6;
  --white:#ffffff;
}
*{box-sizing:border-box;margin:0;padding:0}
html,body{width:822px;height:1200px;overflow:hidden;background:var(--white);font-family:'Poppins',sans-serif;color:var(--ink)}
.page{position:relative;width:822px;height:1200px}
.abs{position:absolute}
.brand{left:60px;top:54px;font-weight:600;font-size:13px;color:var(--ink);display:flex;align-items:center;gap:6px}
.brand .dot{width:10px;height:10px;border-radius:50%;background:var(--orange)}
.brand-tag{left:60px;top:71px;font-size:7.5px;color:var(--ink)}
.nav-bar{left:680px;top:0;width:45px;height:2px;background:var(--orange)}
.nav{top:40px;left:0;font-size:8.5px;font-weight:500}
.nav span{position:absolute;white-space:nowrap}
.search{left:732px;top:32px;width:28px;height:28px;border-radius:50%;background:#ececec;display:flex;align-items:center;justify-content:center}
.page-title{left:0;width:822px;top:96px;text-align:center;font-size:37px;font-weight:700;letter-spacing:.5px}
.accent{color:var(--orange)}
.crumb{left:0;width:822px;top:143px;text-align:center;font-size:11.5px}
.crumb .sep{margin:0 10px}
.rule{left:67px;top:185px;width:700px;height:1px;background:var(--rule)}
.card-shell{left:59px;top:364px;width:229px;height:244px;background:var(--white);border-radius:6px;box-shadow:0 10px 40px rgba(0,0,0,.08)}
.card{left:65px;top:368px;width:217px;height:236px;background:var(--orange);border-radius:6px}
.card-map{left:175px;top:470px;width:98px;height:80px;border-radius:20px;background:rgba(255,255,255,.07)}
.card-title{left:92px;top:402px;font-size:16px;font-weight:600;color:var(--white)}
.info{color:var(--white)}
.info-icon{width:22px;height:22px;border-radius:50%;background:rgba(255,255,255,.25);display:flex;align-items:center;justify-content:center}
.info-label{font-size:9px;font-weight:600}
.info-text{font-size:10px;line-height:12px}
.section-title{left:336px;top:268px;font-size:27px;font-weight:700}
.section-sub{left:336px;top:304px;font-size:11px;color:var(--muted)}
.label{font-size:9px;font-weight:500;color:var(--ink)}
.label b{color:var(--orange);font-weight:500}
.field{background:var(--field);border-radius:5px;font-size:9.5px;color:#666;padding-left:12px;display:flex;align-items:center;font-weight:300}
.field.area{align-items:flex-start;padding-top:12px}
.send-to{left:336px;top:636px;font-size:11px}
.send-to a{color:var(--ink);font-weight:600;text-decoration:none;border-bottom:1px solid var(--ink)}
.btn{left:335px;top:669px;width:172px;height:30px;border-radius:15px;background:var(--orange);color:var(--white);font-size:9.5px;font-weight:600;display:flex;align-items:center;justify-content:center}
.footer{left:0;top:791px;width:822px;height:409px;background:var(--dark)}
.light{color:var(--white)}
.news-title{left:0;width:822px;top:842px;text-align:center;font-size:28px;font-weight:700}
.news-pill{left:190px;top:887px;width:442px;height:42px;border-radius:21px;background:var(--white)}
.news-input{left:226px;top:900px;font-size:11.5px;color:#555}
.news-btn{left:516px;top:893px;width:110px;height:31px;border-radius:16px;background:var(--orange);color:var(--white);font-size:10px;font-weight:600;display:flex;align-items:center;justify-content:center}
.f-mark{left:150px;top:976px;width:20px;height:20px;border-radius:50%;background:var(--orange)}
.f-brand{left:90px;top:1010px;width:140px;text-align:center;font-size:13px;font-weight:600}
.f-tag{left:90px;top:1027px;width:140px;text-align:center;font-size:8px}
.social{width:26px;height:26px;border-radius:50%}
.col-title{font-size:10.5px;font-weight:600}
.col-links{font-size:9.5px;line-height:18.3px;font-weight:300}
.f-contact{font-size:9.5px;font-weight:300;line-height:12px}
.f-map{left:612px;top:1012px;width:122px;height:86px;border-radius:20px;background:rgba(255,255,255,.03)}
.f-rule{left:0;top:1155px;width:822px;height:1px;background:#474747}
.copy{left:0;width:822px;top:1171px;text-align:center;font-size:9px}
.chat{left:770px;top:1137px;width:36px;height:36px;border-radius:50%;background:var(--orange);display:flex;align-items:center;justify-content:center}
</style>
</head>
<body>
<div class="page">
  <div class="abs brand"><span class="dot"></span>LIFTWAVE MEDIA</div>
  <div class="abs brand-tag">Online Marketing. Elevated</div>
  <div class="abs nav-bar"></div>
  <nav class="abs nav">
    <span style="left:390px">HOME</span>
    <span style="left:435px">SERVICES</span>
    <span style="left:496px">FEATURED WORK</span>
    <span style="left:589px">BLOG</span>
    <span style="left:632px">ABOUT</span>
    <span style="left:681px;color:var(--orange)">CONTACT</span>
  </nav>
  <div class="abs search">
    <svg width="11" height="11" viewBox="0 0 12 12"><circle cx="5" cy="5" r="3.8" fill="none" stroke="#333" stroke-width="1.5"/><line x1="8" y1="8" x2="11" y2="11" stroke="#333" stroke-width="1.5"/></svg>
  </div>

  <h1 class="abs page-title"><span class="accent">CONTACT</span> US</h1>
  <div class="abs crumb">
    <svg width="11" height="10" viewBox="0 0 12 11" style="vertical-align:-1px"><path d="M6 0 0 5.5h1.6V11h3.2V7.5h2.4V11h3.2V5.5H12z" fill="#2f2f2f"/></svg>
    Home<span class="sep">|</span>Contact us
  </div>
  <div class="abs rule"></div>

  <div class="abs card-shell"></div>
  <div class="abs card"></div>
  <div class="abs card-map" role="img" aria-label="Faint dotted world map"></div>
  <div class="abs card-title">LIFTWAVE</div>

  <div class="abs info-icon" style="left:92px;top:440px">
    <svg width="9" height="11" viewBox="0 0 10 13"><path d="M5 0a4.5 4.5 0 0 0-4.5 4.5C.5 8 5 13 5 13s4.5-5 4.5-8.5A4.5 4.5 0 0 0 5 0zm0 6.3a1.8 1.8 0 1 1 0-3.6 1.8 1.8 0 0 1 0 3.6z" fill="#fff"/></svg>
  </div>
  <div class="abs info" style="left:121px;top:439px">
    <div class="info-label">LOCATION*</div>
    <div class="info-text">Some address line goes<br>here city name</div>
  </div>

  <div class="abs info-icon" style="left:92px;top:494px">
    <svg width="10" height="10" viewBox="0 0 12 12"><path d="M2.4.3 4.3 2.6 3.3 4.3c.8 1.7 2.6 3.5 4.4 4.4l1.7-1 2.3 1.9-1.2 2.1C5.4 11.8.2 6.6.3 1.5z" fill="#fff"/></svg>
  </div>
  <div class="abs info" style="left:121px;top:490px">
    <div class="info-label">PHONE*</div>
    <div class="info-text">800-555-0142<br>(limited service)</div>
  </div>

  <div class="abs info-icon" style="left:92px;top:546px">
    <svg width="10" height="8" viewBox="0 0 12 9"><path d="M0 0h12v1L6 5 0 1zM0 2.3 6 6.3l6-4V9H0z" fill="#fff"/></svg>
  </div>
  <div class="abs info" style="left:121px;top:542px">
    <div class="info-label">EMAIL*</div>
    <div class="info-text">hello@liftwavemedia.com</div>
  </div>

  <h2 class="abs section-title"><span class="accent">GET</span> IN TOUCH</h2>
  <p class="abs section-sub">Please fill out this form to get in touch with us</p>

  <div class="abs label" style="left:336px;top:344px">Your Name<b>*</b></div>
  <div class="abs label" style="left:552px;top:344px">Your Email<b>*</b></div>
  <div class="abs field" style="left:336px;top:363px;width:209px;height:34px">Enter your name</div>
  <div class="abs field" style="left:552px;top:363px;width:209px;height:34px">Enter your email</div>

  <div class="abs label" style="left:336px;top:413px">Subject<b>*</b></div>
  <div class="abs label" style="left:552px;top:413px">Phone Number<b>*</b></div>
  <div class="abs field" style="left:336px;top:432px;width:209px;height:34px">Enter your subject</div>
  <div class="abs field" style="left:552px;top:432px;width:209px;height:34px">Enter your phone number</div>

  <div class="abs label" style="left:336px;top:482px">Message<b>*</b></div>
  <div class="abs field area" style="left:336px;top:502px;width:424px;height:119px">Type your text...</div>

  <div class="abs send-to">Send the form to <a>hello@liftwavemedia.com</a></div>
  <div class="abs btn">SEND YOUR ENQUIRY NOW</div>

  <footer class="abs footer"></footer>
  <h2 class="abs news-title light"><span class="accent">OUR</span> NEWSLETTER</h2>
  <div class="abs news-pill"></div>
  <svg class="abs" style="left:207px;top:904px" width="13" height="10" viewBox="0 0 12 9"><path d="M0 0h12v1L6 5 0 1zM0 2.3 6 6.3l6-4V9H0z" fill="#bbb"/></svg>
  <div class="abs news-input">Enter your email address</div>
  <div class="abs news-btn">SUBSCRIBE</div>

  <div class="abs f-mark"></div>
  <div class="abs f-brand light">LIFTWAVE MEDIA</div>
  <div class="abs f-tag light">Online Marketing. Elevated.</div>
  <div class="abs social" style="left:113px;top:1050px;background:#3b5998"></div>
  <div class="abs social" style="left:144px;top:1050px;background:#1da1f2"></div>
  <div class="abs social" style="left:174px;top:1050px;background:#d93a2b"></div>

  <div class="abs col-title light" style="left:277px;top:972px">COMPANY</div>
  <div class="abs col-links light" style="left:277px;top:994px">Home<br>Our Services<br>Featured Work<br>Blog<br>About<br>Contact</div>

  <div class="abs col-title light" style="left:427px;top:972px">SUPPORT</div>
  <div class="abs col-links light" style="left:427px;top:1001px">Terms of use<br>Terms &amp; Conditions<br>Privacy Policy<br>Returns<br>Refunds.</div>

  <div class="abs f-map" role="img" aria-label="Faint dotted world map"></div>
  <div class="abs col-title light" style="left:576px;top:972px">CONTACT US</div>
  <svg class="abs" style="left:575px;top:1006px" width="9" height="9" viewBox="0 0 12 12"><path d="M2.4.3 4.3 2.6 3.3 4.3c.8 1.7 2.6 3.5 4.4 4.4l1.7-1 2.3 1.9-1.2 2.1C5.4 11.8.2 6.6.3 1.5z" fill="#ff4707"/></svg>
  <div class="abs f-contact light" style="left:591px;top:1004px">800-555-0142</div>
  <svg class="abs" style="left:575px;top:1033px" width="9" height="7" viewBox="0 0 12 9"><path d="M0 0h12v1L6 5 0 1zM0 2.3 6 6.3l6-4V9H0z" fill="#ff4707"/></svg>
  <div class="abs f-contact light" style="left:591px;top:1030px">info@liftwavemedia.com</div>
  <svg class="abs" style="left:576px;top:1057px" width="7" height="10" viewBox="0 0 10 13"><path d="M5 0a4.5 4.5 0 0 0-4.5 4.5C.5 8 5 13 5 13s4.5-5 4.5-8.5A4.5 4.5 0 0 0 5 0zm0 6.3a1.8 1.8 0 1 1 0-3.6 1.8 1.8 0 0 1 0 3.6z" fill="#ff4707"/></svg>
  <div class="abs f-contact light" style="left:591px;top:1056px">Some address line goes here<br>city name</div>

  <div class="abs f-rule"></div>
  <div class="abs copy light">COPYRIGHT © 2020 LIFTWAVE MEDIA LLC. ALL RIGHTS RESERVED.</div>
  <div class="abs chat">
    <svg width="16" height="14" viewBox="0 0 16 14"><path d="M8 0C3.6 0 0 2.7 0 6c0 1.8 1 3.3 2.6 4.4L2 14l3.6-2.3c.8.2 1.6.3 2.4.3 4.4 0 8-2.7 8-6S12.4 0 8 0z" fill="#fff"/><circle cx="5" cy="6" r="1" fill="#ff4707"/><circle cx="8" cy="6" r="1" fill="#ff4707"/><circle cx="11" cy="6" r="1" fill="#ff4707"/></svg>
  </div>
</div>
</body>
</html>
```